I need a business Card Design for my practice , i am clinical herbalist. I am a herbalist specializing in Lyme disease, autism, autoimmune diseases, difficult to cure diseasesDifficult to cure diseases. In my innovative practice i link traditional medicine, herbs with science, immunologu ,pharmacology.

Industry/Entity Type

Business

Contact Information for Business Card

My company name : OŚRODEK ZIELNIK
My name : Piotr Kaleta
Name of my profession : Fitoterapeuta
In Polish language Fitoterapeuta is Herbalist .

e-mail: piotrkaleta@osrodekzielnik.com
www.osrodek-zielnik.pl
phone : 604 587 231
My company adress : Dąbrowa Sitnicka 41 , 38-415 Lużna
I dont have logo .

Requirements
Nice to have
• My company

```html
<!DOCTYPE html>
<html lang="pl">
<head>
<meta charset="utf-8">
<title>Ośrodek Zielnik – wizytówka</title>
<link rel="stylesheet" href="https://fonts.googleapis.com/css2?family=Lato:wght@400;700&display=swap">
<style>
  :root {
    --herb-green: #00913f;
    --herb-green-soft: #0a9d47;
    --accent-orange: #e07b24;
    --paper: #ffffff;
    --backdrop: #eef1ef;
  }
  * { margin: 0; padding: 0; box-sizing: border-box; }
  html, body { width: 1200px; height: 1000px; overflow: hidden; }
  body {
    background: var(--backdrop);
    font-family: "Lato", Arial, sans-serif;
    position: relative;
  }
  .card {
    position: absolute;
    left: 281px;
    width: 636px;
    height: 371px;
    overflow: hidden;
  }
  .card--front {
    top: 101px;
    background: var(--herb-green);
    display: flex;
    align-items: center;
    justify-content: center;
  }
  .front-name {
    color: var(--paper);
    font-weight: 700;
    font-size: 56px;
    letter-spacing: 1px;
    text-transform: uppercase;
  }
  .card--back {
    top: 528px;
    background: var(--paper);
  }
  .decor-block {
    position: absolute;
    background: var(--herb-green);
  }
  .decor-block--top {
    left: 404px;
    top: 0;
    width: 232px;
    height: 149px;
    border-bottom-left-radius: 60px;
  }
  .decor-block--bottom {
    left: 0;
    top: 196px;
    width: 636px;
    height: 175px;
    border-top-left-radius: 120px;
  }
  .brand-name {
    position: absolute;
    left: 37px;
    top: 40px;
    color: var(--herb-green);
    font-weight: 700;
    font-size: 36px;
    letter-spacing: 0.5px;
    text-transform: uppercase;
    white-space: nowrap;
  }
  .address {
    position: absolute;
    left: 38px;
    top: 98px;
    color: var(--herb-green);
    font-size: 19px;
    line-height: 26px;
    font-style: normal;
  }
  .person {
    position: absolute;
    right: 37px;
    top: 38px;
    text-align: right;
    color: var(--paper);
    font-size: 19px;
    line-height: 26px;
  }
  .person-name { font-weight: 700; }
  .contacts {
    position: absolute;
    right: 37px;
    top: 243px;
    list-style: none;
    color: var(--paper);
    font-size: 19px;
    line-height: 26px;
  }
  .contacts li {
    display: flex;
    justify-content: flex-end;
    align-items: center;
    gap: 6px;
  }
  .contact-icon {
    width: 19px;
    height: 19px;
    background: var(--accent-orange);
    display: inline-flex;
    align-items: center;
    justify-content: center;
  }
  .contact-icon svg { width: 13px; height: 13px; }
</style>
</head>
<body>

  <section class="card card--front" aria-label="Awers wizytówki">
    <h1 class="front-name">Ośrodek Zielnik</h1>
  </section>

  <section class="card card--back" aria-label="Rewers wizytówki">
    <div class="decor-block decor-block--top" role="img" aria-label="Zielony dekoracyjny kształt liścia w prawym górnym rogu"></div>
    <div class="decor-block decor-block--bottom" role="img" aria-label="Zielony dekoracyjny kształt liścia w dolnej części karty"></div>

    <p class="brand-name">Ośrodek Zielnik</p>

    <address class="address">
      Dąbrowa Sitnicka 41<br>
      38-415, Lużna
    </address>

    <div class="person">
      <p class="person-name">Piotr Kaleta</p>
      <p class="person-role">Fitoterapeuta</p>
    </div>

    <ul class="contacts">
      <li>604 587 231
        <span class="contact-icon"><svg viewBox="0 0 13 13"><rect x="4" y="1" width="5" height="11" rx="1" fill="none" stroke="#fff" stroke-width="1.3"/><circle cx="6.5" cy="10" r="0.7" fill="#fff"/></svg></span>
      </li>
      <li>www.osrodek-zielnik.pl
        <span class="contact-icon"><svg viewBox="0 0 13 13"><rect x="1.5" y="2" width="10" height="7" fill="none" stroke="#fff" stroke-width="1.3"/><rect x="5.5" y="9" width="2" height="2" fill="#fff"/><rect x="4" y="11" width="5" height="1" fill="#fff"/></svg></span>
      </li>
      <li>piotrkaleta@osrodekzielnik.com
        <span class="contact-icon"><svg viewBox="0 0 13 13"><rect x="1.5" y="3" width="10" height="7" fill="#fff"/><path d="M1.5,3 L6.5,7 L11.5,3" fill="none" stroke="#e07b24" stroke-width="1"/></svg></span>
      </li>
    </ul>
  </section>

</body>
</html>
```